依頼詳細
スタンダードメニューと特別ページメニューの作成。
スタンダードメニューはフランチャイズ店のようなイメージでお願いします。
参考サイト
https://www.mitsukeru-kensaku.example/search?q=%E5%B1%85%E9%85%92%E5%B1%8B%E3%83%A1%E3%83%8B%E3%83%A5%E3%83%BC&tbm=isch#imgrc=Qx7mTa2Lp9%3Bhttp%253A%252F%252Fimg.tarunikki.example%252Fphoto%252F5.jpg%3Bhttp%253A%252F%252Fkazuenikki.tarunikki.example%252F2011%252F10%252Fpost_17.html
この写真の上の部分の感じです。
料理写真と値段はエクセルで添付致します。
そのほかの写真はホームページから使用してください。
http://www.kurotori-shokudo.example/
料理の説明のあるものもありますので参考にして下さい。
エクセルシート1、2に分けて記載してあります。
よろしくお願い致します。

サイズ
A4
ページ数
6ページ
希望イメージ
シンプル 複雑
単色 カラフル
暗い 明るい
日常 高級
遊び心 厳粛
未来的 伝統的
女性的 男性的
希望する色
赤 黄 黒
納品ファイル
• イラストレーター形式 (.ai)
補足説明
かなり急いでいます。早ければ早いほど助かります。
写真を入れた簡単なイメージだけでも本日12時半頃までに頂けるとそのあとは2、3日の余裕はできます。
宜しくお願いします。

```html
<!DOCTYPE html>
<html lang="ja">
<head>
<meta charset="utf-8">
<title>黒鳥食堂 鍋メニュー</title>
<link rel="stylesheet" href="https://fonts.googleapis.com/css2?family=Shippori+Mincho+B1:wght@600;800&family=Noto+Sans+JP:wght@500;700;900&display=swap">
<style>
  :root {
    --paper: #efe2c6;
    --paper-dark: #dcc39a;
    --red: #c8161d;
    --deep-red: #9e1016;
    --ink: #231815;
    --panel: #fffdf8;
    --olive: #6b8e23;
    --meat: #b5121b;
    --rule: #d8c8a8;
  }
  * { margin: 0; padding: 0; box-sizing: border-box; }
  html, body { width: 846px; height: 1200px; overflow: hidden; }
  body {
    position: relative;
    background: radial-gradient(ellipse at 40% 45%, var(--paper) 0%, var(--paper-dark) 100%);
    font-family: "Noto Sans JP", sans-serif;
    color: var(--ink);
  }
  .shop-name {
    position: absolute; top: 16px; left: 0; width: 100%;
    text-align: center;
    font-family: "Shippori Mincho B1", serif; font-weight: 800;
    font-size: 26px; letter-spacing: 6px;
  }
  .hero-photo {
    position: absolute; top: 60px; left: 330px; width: 516px; height: 580px;
    background: radial-gradient(ellipse at 55% 45%, #e8d6b6 0%, #c9a77a 45%, #8c5c33 80%, rgba(140,92,51,0) 100%);
  }
  .title-mark {
    position: absolute; top: 64px; left: 20px; width: 260px; height: 176px;
    background: linear-gradient(135deg, rgba(200,22,29,0.85), rgba(200,22,29,0.55));
    border-radius: 6px;
  }
  .base-label {
    position: absolute; top: 248px; left: 150px;
    color: var(--red);
    font-family: "Shippori Mincho B1", serif; font-weight: 800; font-size: 30px;
    white-space: nowrap;
    text-shadow: 0 0 4px #fff, 0 0 4px #fff;
  }
  .set-list { position: absolute; top: 320px; left: 48px; list-style: none; }
  .set-list li {
    font-weight: 900; font-size: 22px; line-height: 32px;
    text-shadow: 0 0 4px #fff, 0 0 4px #fff;
  }
  .set-list li::before {
    content: ""; display: inline-block; width: 14px; height: 14px;
    background: var(--red); border-radius: 50%; margin-right: 8px; vertical-align: -1px;
  }
  .set-price {
    position: absolute; top: 418px; left: 56px;
    color: var(--red); font-weight: 900; font-size: 64px; letter-spacing: -1px;
    text-shadow: 0 0 6px #fff, 0 0 6px #fff;
  }
  .set-price small { font-size: 44px; }
  .menu-panel {
    position: absolute; top: 515px; left: 93px; width: 657px; height: 615px;
    background: var(--panel);
    box-shadow: 0 2px 10px rgba(0,0,0,0.25);
    padding: 18px 30px;
  }
  .section-title {
    text-align: center; color: var(--red);
    font-family: "Shippori Mincho B1", serif; font-weight: 800; font-size: 34px;
    line-height: 1.1;
  }
  .section-sub { text-align: center; font-weight: 900; font-size: 20px; margin-bottom: 14px; }
  .columns { display: flex; gap: 28px; }
  .col { flex: 1; list-style: none; min-width: 0; }
  .col li {
    display: flex; justify-content: space-between; align-items: baseline;
    font-weight: 700; font-size: 18px; line-height: 27px;
    border-bottom: 1px dotted var(--rule);
    white-space: nowrap;
  }
  .col li::before {
    content: ""; width: 10px; height: 10px; background: var(--red);
    border-radius: 50%; margin-right: 6px; flex: none; align-self: center;
  }
  .col li .name { flex: 1; }
  .col li .note { font-size: 11px; margin-left: 4px; }
  .col li .price { color: var(--deep-red); }
  .toppings .col:first-child { flex: 1.4; }
  .ingredients .meat-col { flex: 0.85; }
  .ingredients .veg-col { flex: 1.15; }
  .divider { height: 2px; background: var(--red); margin: 22px 0 10px; }
  .badge {
    display: inline-block; padding: 2px 26px; margin-bottom: 8px;
    color: #fff; font-weight: 900; font-size: 18px; border-radius: 3px;
  }
  .badge.meat { background: var(--meat); }
  .badge.veg { background: var(--olive); }
  .col-head { text-align: center; }
  .veg-set { font-weight: 900; font-size: 18px; display: flex; justify-content: space-between; }
  .veg-note { font-size: 11px; color: #555; margin-bottom: 4px; }
  .veg-grid { display: grid; grid-template-columns: 1fr 1fr; column-gap: 12px; list-style: none; }
  .veg-grid li { font-size: 15px; }
  .veg-grid li::before { width: 8px; height: 8px; margin-right: 4px; }
  .veg-grid li .price { color: var(--deep-red); margin-left: 4px; }
</style>
</head>
<body>
  <div class="hero-photo" role="img" aria-label="鶏肉と野菜がたっぷり入った土鍋の写真"></div>
  <div class="shop-name">黒鳥食堂</div>
  <div class="title-mark" role="img" aria-label="毛筆で書かれた「鍋」の大きな文字"></div>
  <div class="base-label">鶏がらベース</div>
  <ul class="set-list">
    <li>味噌ちゃんこ鍋 1人前</li>
    <li>塩ちゃんこ鍋 1人前</li>
    <li>チゲちゃんこ鍋 1人前</li>
  </ul>
  <div class="set-price">2098<small>円</small></div>

  <section class="menu-panel">
    <h2 class="section-title">トッピング</h2>
    <p class="section-sub">鍋後のお食事&amp;味の変化</p>
    <div class="columns toppings">
      <ul class="col">
        <li><span class="name">カルボナーラ<span class="note">1人前セット</span></span><span class="price">546円</span></li>
        <li><span class="name">ラーメン<span class="note">セット</span></span><span class="price">299円</span></li>
        <li><span class="name">きしめん<span class="note">セット</span></span><span class="price">299円</span></li>
        <li><span class="name">雑炊<span class="note">セット</span></span><span class="price">257円</span></li>
        <li><span class="name">長芋とろろ</span><span class="price">499円</span></li>
      </ul>
      <ul class="col">
        <li><span class="name">柚子こしょう</span><span class="price">302円</span></li>
        <li><span class="name">チーズ</span><span class="price">205円</span></li>
        <li><span class="name">バター</span><span class="price">199円</span></li>
        <li><span class="name">ヤンニン</span><span class="price">199円</span></li>
        <li><span class="name">カレー粉</span><span class="price">199円</span></li>
        <li><span class="name">キムチ</span><span class="price">199円</span></li>
      </ul>
    </div>

    <div class="divider"></div>
    <h2 class="section-title">鍋の具材追加</h2>
    <div class="columns ingredients" style="margin-top:10px">
      <div class="col meat-col">
        <div class="col-head"><span class="badge meat">肉</span></div>
        <ul class="col">
          <li><span class="name">ももステーキ<span class="note">(1枚)</span></span><span class="price">499円</span></li>
          <li><span class="name">肉 盛り合わせ</span><span class="price">998円</span></li>
          <li><span class="name">特製つくね</span><span class="price">499円</span></li>
          <li><span class="name">もも肉</span><span class="price">499円</span></li>
          <li><span class="name">むね肉</span><span class="price">499円</span></li>
          <li><span class="name">ねぎ肉</span><span class="price">499円</span></li>
        </ul>
      </div>
      <div class="col veg-col">
        <div class="col-head"><span class="badge veg">野菜</span></div>
        <div class="veg-set"><span>野菜盛り合わせ</span><span>950円</span></div>
        <p class="veg-note">白菜・人参・もやし・豆腐など</p>
        <ul class="veg-grid">
          <li><span class="name">にんじん</span><span class="price">199円</span></li>
          <li><span class="name">白菜</span><span class="price">298円</span></li>
          <li><span class="name">豆腐</span><span class="price">199円</span></li>
          <li><span class="name">にんにん</span><span class="price">298円</span></li>
          <li><span class="name">もやし</span><span class="price">199円</span></li>
          <li><span class="name">水菜</span><span class="price">298円</span></li>
          <li><span class="name">キャベツ</span><span class="price">298円</span></li>
          <li><span class="name">えのき</span><span class="price">298円</span></li>
          <li><span class="name">じゃがいも</span><span class="price">298円</span></li>
          <li><span class="name">しめじ</span><span class="price">325円</span></li>
        </ul>
      </div>
    </div>
  </section>
</body>
</html>
```